PSD Designs needed to give to my Developer

Hello, I need PSD files to give to my programmer for the creation of my new website. The website is for ORA quarter, a new clothing company based in Chicago, IL. We sell womens, mens and kids fashion. We specialize in jackets, outerwear and sweaters, but we sell clothing from every category, I have someone working on the logo, so I can't include it for reference. However, I have included 2 reference sites as well as a PDF of how the 2 reference sites could be merged together. The main company color should be blue (hence the name ORA quarter), and the overall feel of the site should be FUN. It should communicate: This is where you want to shop if you want a FUN, HAPPY experience. I need the Home Page file designed very quickly. Whoever is awarded this job will immediately continue working with me to design the other 8 pages. I will pay for all pages. The amount I am offering is for this one page only, and I will pay you additional to design all other 8 pages. Thank you for your time and I will be picking the best design so that we can immediately build a great relationship and work through the rest of the project.

Industry/Entity Type

Apparel Store

Number of Pages Required

1 page

Font styles to use
Sans Serif

Colors
33a6d7
0492cd
ffffff

Requirements
Must have
• I have included all notes in the project description so please check there. My project must communicate: Fun and Happy Design. Even tho I have chosen a few variations of blue below, I still want the designer to incorporate other colors as necessary to acheive the desired look.
Should not have
• It should have a boring, childish feel

```html
<!DOCTYPE html>
<html lang="en">
<head>
<meta charset="utf-8">
<title>ORA quarter — Home</title>
<link rel="stylesheet" href="https://fonts.googleapis.com/css2?family=Antonio:wght@200;300&family=Arimo:wght@700&display=swap">
<style>
  :root {
    --blue: #0898cb;
    --blue-soft: #33a6d7;
    --blue-deep: #0492cd;
    --nav-blue: #1a95cc;
    --white: #ffffff;
    --glow: rgba(110, 200, 220, 0.55);
    --page-top: #eef5f7;
    --page-mid: #dbe9ee;
  }
  * { box-sizing: border-box; margin: 0; padding: 0; }
  html, body { width: 1200px; height: 1000px; overflow: hidden; }
  body {
    position: relative;
    font-family: "Arimo", Arial, sans-serif;
    font-weight: 700;
    color: var(--nav-blue);
    background: var(--white);
  }
  .page-backdrop {
    position: absolute; inset: 0;
    background: radial-gradient(ellipse at 50% 45%, #f7fbfc 0%, var(--page-top) 45%, var(--page-mid) 100%);
  }
  .promo-bar {
    position: absolute; left: 29px; top: 17px; width: 1139px; height: 40px;
    background: var(--blue);
    color: var(--white);
  }
  .promo-bar__offer { position: absolute; left: 12px; top: 9px; font-size: 21px; }
  .promo-bar__login { position: absolute; left: 797px; top: 8px; font-size: 19px; }
  .social-links { position: absolute; left: 958px; top: 5px; display: flex; gap: 10px; }
  .social-links__item { width: 30px; height: 30px; border-radius: 50%; background: var(--white); }

  .main-nav, .footer-nav { position: absolute; font-size: 17px; }
  .main-nav { top: 102px; left: 0; width: 780px; height: 30px; }
  .main-nav a, .footer-nav a { position: absolute; color: var(--nav-blue); text-decoration: none; white-space: nowrap; }
  .main-nav a.is-active { color: #0a7fb5; }
  .main-nav a.is-active::after {
    content: ""; position: absolute; left: 0; right: 0; top: 24px; height: 4px; background: #0a7fb5;
  }
  .brand-mark {
    position: absolute; left: 780px; top: 76px; width: 380px;
    text-align: center; font-size: 41px; line-height: 53px; color: var(--blue-deep);
  }

  .photo { position: absolute; overflow: hidden; box-shadow: 0 0 30px var(--glow); }
  .hero-portrait {
    left: 82px; top: 143px; width: 360px; height: 358px; border-radius: 50%;
    background: radial-gradient(circle at 40% 30%, #8c6a4c 0%, #4f5a3f 40%, #7f93a8 65%, #2d3326 100%);
  }
  .hero-slide {
    left: 509px; top: 203px; width: 582px; height: 234px; border-radius: 8px;
    background: linear-gradient(100deg, #3d3327 0%, #6d5a43 35%, #a58c6c 65%, #584636 100%);
  }
  .tile { top: 513px; width: 577px; height: 192px; border-radius: 8px; }
  .tile--story { left: 23px; background: linear-gradient(180deg, #3a4258 0%, #b14a5c 30%, #8f8a80 60%, #5e6a58 85%, #8c8a82 100%); }
  .tile--shop { left: 611px; background: linear-gradient(110deg, #b6b8bc 0%, #46587a 35%, #9aa2ad 60%, #b98a55 80%, #e6e3de 100%); }
  .movement-banner {
    left: 23px; top: 732px; width: 1165px; height: 189px; border-radius: 8px;
    background: linear-gradient(90deg, #aab7bf 0%, #6f7880 30%, #c9a58c 50%, #6d6f72 70%, #b3bcc2 100%);
  }

  .display {
    position: absolute; font-family: "Antonio", "Arial Narrow", sans-serif; font-weight: 200;
    line-height: 1; white-space: nowrap; paint-order: stroke fill;
    -webkit-text-stroke: 5px var(--blue-deep); color: var(--white);
    transform-origin: left top; transform: scaleX(var(--squeeze, 1));
  }
  .display--inverse { -webkit-text-stroke: 5px var(--white); color: var(--blue-deep); }
  .hero-slide .display--ladies { left: 21px; top: 11px; font-size: 133px; --squeeze: 0.72; }
  .hero-slide .display--shopping { left: 299px; top: 11px; font-size: 133px; --squeeze: 0.6; }
  .hero-slide .display--tagline { left: 111px; top: 172px; font-size: 44px; -webkit-text-stroke: 3px var(--blue-deep); --squeeze: 0.8; }
  .tile .display { top: 13px; font-size: 155px; color: #fbeff2; }
  .tile--story .display { left: 55px; --squeeze: 0.69; }
  .tile--shop .display { left: 179px; --squeeze: 0.65; }
  .movement-banner .display { left: 162px; top: 54px; font-size: 113px; color: #eef3f6; --squeeze: 0.69; }

  .slider-dots { position: absolute; left: 578px; top: 474px; display: flex; gap: 9px; }
  .slider-dots span { width: 13px; height: 13px; border-radius: 50%; border: 2px solid var(--blue-deep); background: var(--white); }
  .slider-dots span.is-current { background: radial-gradient(circle, var(--blue-deep) 0 3px, var(--white) 3.5px); }

  .footer-nav { top: 941px; left: 0; width: 1200px; height: 22px; }
  .copyright { position: absolute; top: 969px; left: 0; width: 1318px; text-align: center; font-size: 17px; color: var(--nav-blue); }
</style>
</head>
<body>
  <div class="page-backdrop" role="img" aria-label="Faded shopping mall interior backdrop"></div>

  <header>
    <div class="promo-bar">
      <span class="promo-bar__offer">Pop-up your own ORA Boulevard for ONLY $99</span>
      <span class="promo-bar__login">Stylist Login</span>
      <div class="social-links" aria-label="Social profiles">
        <span class="social-links__item" aria-label="Social profile 1"></span>
        <span class="social-links__item" aria-label="Social profile 2"></span>
        <span class="social-links__item" aria-label="Social profile 3"></span>
        <span class="social-links__item" aria-label="Social profile 4"></span>
      </div>
    </div>

    <nav class="main-nav">
      <a class="is-active" href="#" style="left:32px">HOME</a>
      <a href="#" style="left:105px">GET TO KNOW US</a>
      <a href="#" style="left:291px">WHY ORA?</a>
      <a href="#" style="left:415px">HOST A POP-UP</a>
      <a href="#" style="left:583px">BECOME A STYLIST</a>
    </nav>

    <div class="brand-mark">ORA quarter logo<br>here</div>
  </header>

  <main>
    <div class="photo hero-portrait" role="img" aria-label="Young woman in a brown wide-brim hat and light blue crop top"></div>

    <div class="photo hero-slide" role="img" aria-label="Shopper browsing clothes on a rack">
      <span class="display display--ladies">LADIES</span>
      <span class="display display--inverse display--shopping">SHOPPING</span>
      <span class="display display--tagline">SHOP HERE IF YOU WANT A FUN</span>
    </div>

    <div class="slider-dots" aria-label="Slides">
      <span></span><span class="is-current"></span><span></span><span></span>
    </div>

    <a class="photo tile tile--story" href="#" role="img" aria-label="Stack of folded knit sweaters">
      <span class="display">OUR STORY</span>
    </a>
    <a class="photo tile tile--shop" href="#" role="img" aria-label="Shirts hanging on wooden hangers">
      <span class="display">SHOP</span>
    </a>

    <div class="photo movement-banner" role="img" aria-label="Three smiling friends in beanies">
      <span class="display">BE HAPPIER, JOIN THE MOUVEMENT</span>
    </div>
  </main>

  <footer>
    <nav class="footer-nav">
      <a href="#" style="left:247px">HOME</a>
      <a href="#" style="left:319px">GET TO KNOW US</a>
      <a href="#" style="left:506px">WHY ORA?</a>
      <a href="#" style="left:630px">HOST A POP-UP</a>
      <a href="#" style="left:798px">BECOME A STYLIST</a>
    </nav>
    <p class="copyright">© 2018 ORA Quarter Chicqgo IL. All Rights Reserve</p>
  </footer>
</body>
</html>
```